Garage Door Business Truck Wrap

looking to create a wrap for a 2012 brannock velmaro 2500 HD single cab with service bed. please use creativity, here is the website www.halvordgaragedoorservices.com.. Also, I will upload documents of branded items, Id like everything to seamlessly flow together

```html
<!DOCTYPE html>
<html lang="en">
<head>
<meta charset="utf-8">
<title>Halvord Doors – Service Truck Wrap, Driver Side</title>
<link rel="stylesheet" href="https://fonts.googleapis.com/css2?family=Montserrat:wght@600;700;800&family=Roboto+Condensed:ital,wght@0,700;1,700&display=swap">
<style>
  :root {
    --backdrop: #8d8e92;
    --wrap-black: #0d0c0b;
    --glass: #2b333c;
    --rail: #c9cacc;
    --gold: #c9a53e;
    --gold-bright: #e0c25a;
    --cream: #e6dcc6;
    --silver-text: #d8d8d8;
  }
  * { margin: 0; padding: 0; box-sizing: border-box; }
  html, body { width: 1200px; height: 810px; overflow: hidden; background: var(--backdrop); }
  .canvas { position: relative; width: 1200px; height: 810px; }
  .wrap-art { position: absolute; inset: 0; }

  .text { position: absolute; white-space: nowrap; }

  .emergency {
    left: 101px; top: 361px;
    font: 700 14px/1 "Montserrat", sans-serif;
    color: var(--cream);
    letter-spacing: 0.2px;
  }
  .brand-name {
    left: 372px; top: 434px;
    font: 700 21px/1 "Montserrat", sans-serif;
    color: var(--cream);
    letter-spacing: 0.5px;
  }

  .credentials {
    left: 634px; top: 330px;
    font: italic 700 13px/16px "Roboto Condensed", sans-serif;
    color: var(--silver-text);
    text-transform: uppercase;
  }
  .credentials span { display: block; }
  .credentials span + span { padding-left: 14px; }

  .service-list {
    position: absolute; left: 623px; top: 371px; width: 132px;
    list-style: none;
  }
  .service-list li {
    font: 700 14px/1 "Roboto Condensed", sans-serif;
    color: var(--gold-bright);
    height: 27.5px; padding: 4px 0 0 2px;
    border-bottom: 1px solid #9a9a9a;
    white-space: nowrap;
  }
  .service-list li:last-child { border-bottom: 0; }

  .phone {
    left: 767px; top: 340px;
    font: 800 29px/1 "Montserrat", sans-serif;
    color: var(--gold);
    letter-spacing: -0.5px;
  }
  .tagline {
    left: 768px; top: 378px;
    font: 600 10.5px/1 "Montserrat", sans-serif;
    color: var(--gold);
    letter-spacing: 0.2px;
  }
</style>
</head>
<body>
<main class="canvas">
  <svg class="wrap-art" width="1200" height="810" viewBox="0 0 1200 810" aria-hidden="true">
    <defs>
      <linearGradient id="emergency-band" x1="0" x2="1">
        <stop offset="0" stop-color="#8a7336"/>
        <stop offset="0.6" stop-color="#5c4d26"/>
        <stop offset="1" stop-color="#0d0c0b" stop-opacity="0"/>
      </linearGradient>
      <linearGradient id="bed-sweep" x1="0" y1="1" x2="1" y2="0">
        <stop offset="0" stop-color="#b08d2c"/>
        <stop offset="0.5" stop-color="#7d6520"/>
        <stop offset="1" stop-color="#c9a53e"/>
      </linearGradient>
      <clipPath id="cab-shape">
        <path d="M68,352 Q72,338 120,330 L310,318 Q360,280 400,258 Q440,236 500,231 L572,229 Q590,231 591,250 L591,506 L300,506 Q294,410 205,405 Q126,406 118,470 L112,515 L68,505 Z"/>
      </clipPath>
      <clipPath id="bed-shape">
        <path d="M609,316 L1127,322 L1122,510 L965,510 Q958,438 868,436 Q782,438 772,510 L609,510 Z"/>
      </clipPath>
    </defs>

    <g class="cab-panel" clip-path="url(#cab-shape)">
      <rect x="60" y="220" width="540" height="300" fill="var(--wrap-black)"/>
      <path class="cab-window" d="M345,336 L362,300 Q395,262 440,248 Q480,243 530,243 Q538,246 537,256 L533,334 Z" fill="var(--glass)"/>
      <rect class="emergency-band" x="86" y="356" width="300" height="26" fill="url(#emergency-band)"/>
      <rect x="86" y="380" width="290" height="2" fill="var(--gold)" opacity="0.8"/>
      <path class="cab-swoosh" d="M288,462 Q420,497 592,492 L592,510 L300,510 Z" fill="var(--gold)"/>
    </g>

    <rect class="bed-top-rail" x="609" y="294" width="522" height="22" fill="var(--rail)"/>
    <g class="bed-panel" clip-path="url(#bed-shape)">
      <rect x="600" y="310" width="540" height="210" fill="var(--wrap-black)"/>
      <path class="bed-low-swoosh" d="M609,498 Q700,492 800,478 L800,512 L609,512 Z" fill="var(--gold)"/>
      <path class="bed-sweep" d="M900,480 Q1030,425 1130,322 L1130,512 L900,512 Z" fill="url(#bed-sweep)"/>
      <path class="bed-sweep-stripe" d="M935,472 Q1050,420 1130,360 L1130,392 Q1050,448 960,488 Z" fill="#2a2412" opacity="0.9"/>
    </g>
    <rect class="bed-bottom-rail" x="609" y="500" width="165" height="8" fill="var(--rail)"/>
    <rect class="bed-bottom-rail" x="965" y="502" width="160" height="8" fill="var(--rail)"/>
  </svg>

  <p class="text emergency">24/7 EMERGENCY SERVICE</p>
  <p class="text brand-name">HALVORD DOORS</p>

  <p class="text credentials"><span>Commercial</span><span>&amp; Licensed</span></p>
  <ul class="service-list">
    <li>Garage Doors</li>
    <li>Garage Door Openers</li>
    <li>Roll-Up Garage Door</li>
    <li>Retractable Screens</li>
  </ul>

  <p class="text phone">(555) 014-2290</p>
  <p class="text tagline">RESIDENTIAL GARAGE DOOR SERVICE</p>
</main>
</body>
</html>
```